Velmora Water Purification

We need a website set up on a "Free account" WordPress platform. (This is the type of Wordpress site that you can sign up for and create online for free (not a server-hosted type.)
The website will be for a water purification company. They install devices in homes to purify the water for safer drinking, bathing, and cleaning.
Our logo is attached. Please keep color scheme of the website consistent with the logo.
Water Purification

```html
<!DOCTYPE html>
<html lang="en">
<head>
<meta charset="utf-8">
<title>Velmora Water Purification</title>
<link rel="stylesheet" href="https://fonts.googleapis.com/css2?family=Mulish:ital,wght@0,400;0,600;0,700;0,800;1,400&family=Open+Sans:ital,wght@0,400;0,600;1,400&display=swap">
<style>
  :root{
    --sky:#3aa0dc;
    --sky-light:#5fb3e6;
    --navy:#1f3d78;
    --navy-deep:#183263;
    --ink:#2b2b2b;
    --grey-text:#777;
    --pale:#ededed;
    --white:#fff;
  }
  *{box-sizing:border-box;margin:0;padding:0}
  html,body{width:1200px;height:3237px;overflow:hidden}
  body{position:relative;background:var(--white);font-family:"Open Sans",sans-serif;color:var(--ink)}
  .abs{position:absolute}

  /* header */
  .site-header{left:0;top:0;width:1200px;height:108px;background:var(--white);z-index:3}
  .brand{left:118px;top:30px;display:flex;align-items:center;gap:12px}
  .brand-dot{width:34px;height:34px;border-radius:50%;background:var(--sky)}
  .brand-name{font-family:"Mulish",sans-serif;font-weight:800;font-size:32px;color:var(--navy)}
  .main-nav{right:123px;top:47px;display:flex;gap:32px;font-family:"Mulish",sans-serif;font-size:15px;font-weight:600;color:#7a7a7a;text-transform:uppercase}
  .main-nav .current{color:var(--navy)}

  /* hero */
  .hero{left:0;top:108px;width:1200px;height:560px}
  .hero-photo{width:100%;height:100%;background:linear-gradient(100deg,#c9a78d 0%,#e4d3c6 25%,#8fbf6c 45%,#5d9c3e 70%,#78b254 100%)}
  .hero-curve{left:0;top:560px;width:1200px;height:120px}
  .hero-title{left:686px;top:262px;font-family:"Mulish",sans-serif;font-weight:800;font-size:42px;line-height:46px;color:var(--white)}
  .btn-outline-light{left:690px;top:423px;width:158px;height:50px;border:2px solid var(--white);border-radius:25px;color:var(--white);font-family:"Mulish",sans-serif;font-weight:700;font-size:17px;display:flex;align-items:center;justify-content:center}

  /* features */
  .feature{width:294px;height:294px;border-radius:50%;background:var(--sky);color:var(--white);text-align:center;padding-top:64px;z-index:2}
  .feature.dark{background:var(--navy)}
  .feature svg{width:62px;height:62px}
  .feature h3{font-family:"Mulish",sans-serif;font-weight:700;font-size:23px;margin-top:18px}
  .feature p{font-size:12.5px;line-height:18px;width:190px;margin:12px auto 0;opacity:.9}

  /* about */
  .about{left:0;top:945px;width:1200px;height:475px;background:var(--pale)}
  .about-photo{left:550px;top:0;width:650px;height:475px;background:linear-gradient(90deg,#efefef 0%,#e0e3e5 40%,#8fc1dc 70%,#d7d9db 100%)}
  .section-title{font-family:"Mulish",sans-serif;font-weight:700;font-size:32px}
  .about .section-title{left:121px;top:108px;color:var(--navy)}
  .body-copy{font-size:13.5px;line-height:23px;color:var(--grey-text)}
  .about .body-copy{left:121px;width:420px}
  .btn-outline-navy{width:160px;height:48px;border:2px solid var(--navy);border-radius:24px;color:var(--navy);font-family:"Mulish",sans-serif;font-weight:700;font-size:15px;display:flex;align-items:center;justify-content:center}

  /* why */
  .why{left:0;top:1420px;width:1200px;height:475px;background:linear-gradient(90deg,var(--sky) 0%,#4aa8e2 60%,#5db4e8 100%)}
  .why .section-title{left:585px;top:92px;color:var(--white)}
  .why .body-copy{left:585px;width:480px;color:#e6f3fb}
  .btn-outline-white{left:585px;top:330px;width:160px;height:48px;border:2px solid var(--white);border-radius:24px;color:var(--white);font-family:"Mulish",sans-serif;font-weight:700;font-size:15px;display:flex;align-items:center;justify-content:center}

  /* testimonials */
  .testimonials{left:0;top:1895px;width:1200px;height:415px;background:var(--pale)}
  .testimonials .section-title{left:0;width:1200px;top:62px;text-align:center;color:#333}
  .avatar{left:261px;top:134px;width:172px;height:172px;border-radius:50%;border:5px solid var(--white);box-shadow:0 0 0 3px var(--sky);background:linear-gradient(160deg,#e8e6e4,#c9b3a3)}
  .quote{left:470px;top:150px;width:515px;font-style:italic;font-size:14.5px;line-height:29px;color:#666}
  .quote-mark{position:absolute;font-family:Georgia,serif;font-style:normal;font-size:44px;line-height:1;color:#333}
  .quote-mark.open{left:-22px;top:-8px}
  .quote-mark.close{right:-4px;bottom:-22px}
  .quote-author{left:472px;top:265px;font-family:"Mulish",sans-serif;font-size:18px;color:#222}
  .dots{left:557px;top:357px;display:flex;gap:8px}
  .dots span{width:14px;height:14px;border-radius:50%;background:#bdbdbd}
  .dots span.on{background:var(--white);border:2px solid #bdbdbd}

  /* contact cta */
  .cta-photo{left:117px;top:2367px;width:481px;height:328px;background:linear-gradient(120deg,#8a6a52 0%,#c9b9a4 40%,#3e63a8 70%,#d9d3ca 100%)}
  .cta-title{left:648px;top:2374px;font-family:"Mulish",sans-serif;font-weight:700;font-size:28px;color:var(--navy)}
  .cta-sub{left:648px;top:2414px;font-family:"Mulish",sans-serif;font-weight:700;font-size:22px;color:var(--navy)}
  .cta .body-copy{left:648px;width:420px}
  .btn-solid{left:648px;top:2622px;width:160px;height:48px;border-radius:24px;background:var(--sky);color:var(--white);font-family:"Mulish",sans-serif;font-weight:700;font-size:15px;display:flex;align-items:center;justify-content:center}

  /* footer */
  .footer-curve{left:0;top:2745px;width:1200px;height:90px}
  .site-footer{left:0;top:2830px;width:1200px;height:331px;background:var(--navy)}
  .footer-col{top:62px;color:var(--white)}
  .footer-col h4{font-family:"Mulish",sans-serif;font-weight:700;font-size:17px;margin-bottom:18px}
  .footer-col li{list-style:none;font-size:14px;line-height:26px}
  .contact-row{display:flex;gap:12px;font-size:15px;line-height:26px;margin-bottom:4px}
  .contact-row svg{width:18px;height:18px;margin-top:4px;flex:none}
  .social{display:flex;gap:8px}
  .social span{width:38px;height:38px;border:2px solid var(--white);border-radius:50%}
  .legal-bar{left:0;top:3161px;width:1200px;height:76px;background:var(--navy-deep);color:#c9d3e6;font-size:12.5px;text-align:center;line-height:66px}
</style>
</head>
<body>

<header class="site-header abs">
  <div class="brand abs"><span class="brand-dot"></span><span class="brand-name">Velmora</span></div>
  <nav class="main-nav abs">
    <span class="current">Home</span><span>About Us</span><span>Services</span><span>Water Purification</span><span>Why Us</span><span>Contact</span>
  </nav>
</header>

<section class="hero abs">
  <div class="hero-photo" role="img" aria-label="Photo of a young girl drinking a glass of clean water outdoors against green foliage"></div>
</section>
<svg class="hero-curve abs" viewBox="0 0 1200 120" preserveAspectRatio="none" aria-hidden="true">
  <path d="M0 0 Q600 70 1200 -10 L1200 120 L0 120Z" fill="#fff"/>
  <path d="M0 0 Q600 70 1200 -10" fill="none" stroke="#3aa0dc" stroke-width="3"/>
</svg>
<h1 class="hero-title abs">We Installs Water<br>Purification<br>Systems in homes</h1>
<div class="btn-outline-light abs">Contact Us</div>

<div class="feature abs" style="left:138px;top:619px">
  <svg viewBox="0 0 64 64" fill="none" stroke="#fff" stroke-width="3"><path d="M14 8h36l-4 50H18z"/><path d="M16 26h32l-3 30H19z" fill="#fff"/></svg>
  <h3>Safe Drinking</h3>
  <p>alesuada ut tincidunt sed diam Donec quis mi sed magna hendrerit accumsan</p>
</div>
<div class="feature dark abs" style="left:461px;top:619px">
  <svg viewBox="0 0 64 64" fill="none" stroke="#fff" stroke-width="3"><circle cx="28" cy="28" r="18"/><path d="M41 41l15 15"/><circle cx="24" cy="24" r="4"/><circle cx="33" cy="31" r="3"/><path d="M24 20v-5M33 28l4-4M20 24h-5"/></svg>
  <h3>100% Germs Free</h3>
  <p>alesuada ut tincidunt sed diam Donec quis mi sed magna hendrerit accumsan</p>
</div>
<div class="feature abs" style="left:776px;top:619px">
  <svg viewBox="0 0 64 64" fill="none" stroke="#fff" stroke-width="3"><path d="M6 32h52M10 32v10a10 10 0 0 0 10 10h24a10 10 0 0 0 10-10V32M18 52l-3 6M46 52l3 6M14 32V12a5 5 0 0 1 10 0"/></svg>
  <h3>Safe Bathing</h3>
  <p>alesuada ut tincidunt sed diam Donec quis mi sed magna hendrerit accumsan</p>
</div>

<section class="about abs">
  <div class="about-photo abs" role="img" aria-label="Photo of a smiling woman filling a glass from a kitchen tap"></div>
  <h2 class="section-title abs">Velmora Water Purification</h2>
  <p class="body-copy abs" style="top:170px">Vivamus porttitor purus nisi eleifend libero a tempus libero lectus feugiat felis Morbi diam mauris viverra in gravida eu mattis in ante Morbi eget arcu Morbi porta libero</p>
  <p class="body-copy abs" style="top:255px">mollis aliquam Curabitur iaculis tempus eros Curabitur vel mi sit amet magna malesuada ultrices</p>
  <div class="btn-outline-navy abs" style="left:121px;top:326px">READ MORE</div>
</section>

<section class="why abs">
  <svg class="abs" style="left:158px;top:18px" width="410" height="440" viewBox="0 0 410 440" role="img" aria-label="Water-drop shaped photos of hands passing a glass of water and a filter cartridge">
    <defs><linearGradient id="dropFill" x1="0" y1="0" x2="1" y2="1"><stop offset="0" stop-color="#a6d36a"/><stop offset="1" stop-color="#6fa842"/></linearGradient></defs>
    <path d="M150 8 C190 90 290 190 290 290 A140 140 0 0 1 10 290 C10 190 110 90 150 8Z" fill="url(#dropFill)" stroke="#fff" stroke-width="8"/>
    <path d="M320 118 C340 160 380 200 380 240 A62 62 0 0 1 256 240 C256 200 300 160 320 118Z" fill="#7fa8c6" stroke="#fff" stroke-width="7"/>
  </svg>
  <h2 class="section-title abs">Why Choose Us</h2>
  <p class="body-copy abs" style="top:155px">Vivamus porttitor purus nisi eleifend libero a tempus libero lectus feugiat felis Morbi diam mauris viverra in gravida eu mattis in ante Morbi eget arcu Morbi porta libero id ullamcorper nonummy nibh ligula pulvinar metus eget consectetuer augue nisi quis lacus</p>
  <p class="body-copy abs" style="top:257px">mollis aliquam Curabitur iaculis tempus eros Curabitur vel mi sit amet magna malesuada ultrices Ut nisi erat fermentum vel congue</p>
  <div class="btn-outline-white abs">READ MORE</div>
</section>

<section class="testimonials abs">
  <h2 class="section-title abs">Testimonials</h2>
  <div class="avatar abs" role="img" aria-label="Circular portrait of a satisfied customer"></div>
  <p class="quote abs"><span class="quote-mark open">&ldquo;</span>Vivamus porttitor purus nisi eleifend libero a tempus libero lectus feugiat felis Morbi diam mauris viverra in gravida eu mattis in ante Morbi eget arcu Morbi porta libero id ullamcorper nonummy nib<span class="quote-mark close">&rdquo;</span></p>
  <p class="quote-author abs">By Author Name</p>
  <div class="dots abs"><span class="on"></span><span></span><span></span><span></span></div>
</section>

<section class="cta">
  <div class="cta-photo abs" role="img" aria-label="Photo of a technician in overalls installing an under-sink water filtration unit"></div>
  <h2 class="cta-title abs">Contact Us Now for Installs</h2>
  <h3 class="cta-sub abs">Water purification systems</h3>
  <p class="body-copy abs" style="top:2466px">Vivamus porttitor purus nisi eleifend libero a tempus libero lectus feugiat felis Morbi diam mauris viverra in gravida eu mattis in ante Morbi eget arcu Morbi porta libero</p>
  <p class="body-copy abs" style="top:2546px">mollis aliquam Curabitur iaculis tempus eros Curabitur vel mi sit amet magna malesuada ultrices</p>
  <div class="btn-solid abs">CLICK HERE</div>
</section>

<svg class="footer-curve abs" viewBox="0 0 1200 90" preserveAspectRatio="none" aria-hidden="true">
  <path d="M0 10 Q600 80 1200 10 L1200 90 L0 90Z" fill="#1f3d78"/>
  <path d="M0 22 Q600 92 1200 22" fill="none" stroke="#3aa0dc" stroke-width="4"/>
</svg>
<footer class="site-footer abs">
  <div class="footer-col abs" style="left:121px">
    <h4>QUICK LINKS</h4>
    <ul><li>Home</li><li>About Us</li><li>Why Us</li><li>Testimonials</li></ul>
  </div>
  <div class="footer-col abs" style="left:341px">
    <h4>RESOURCES</h4>
    <ul><li>Water Purification</li><li>Blogs</li><li>Contact Us</li></ul>
  </div>
  <div class="footer-col abs" style="left:565px">
    <h4>CONTACT INFO</h4>
    <div class="contact-row"><svg viewBox="0 0 24 24" fill="#fff"><path d="M12 2a7 7 0 0 0-7 7c0 5 7 13 7 13s7-8 7-13a7 7 0 0 0-7-7zm0 9.5A2.5 2.5 0 1 1 12 6.5a2.5 2.5 0 0 1 0 5z"/></svg><span>48 Larkspur Avenue #4B<br>Austin 78701 TX</span></div>
    <div class="contact-row"><svg viewBox="0 0 24 24" fill="none" stroke="#fff" stroke-width="2"><path d="M5 3h4l2 5-2.5 1.5a11 11 0 0 0 6 6L16 13l5 2v4a2 2 0 0 1-2 2A16 16 0 0 1 3 5a2 2 0 0 1 2-2z"/></svg><span>512.555.0148</span></div>
    <div class="contact-row"><svg viewBox="0 0 24 24" fill="none" stroke="#fff" stroke-width="2"><rect x="3" y="5" width="18" height="14" rx="1"/><path d="M3 6l9 7 9-7"/></svg><span>info@velmorawater.com</span></div>
  </div>
  <div class="footer-col abs" style="left:842px">
    <h4>FOLLOW US</h4>
    <div class="social"><span></span><span></span><span></span><span></span></div>
  </div>
</footer>
<div class="legal-bar abs">© 2017 Velmora Water Purification &nbsp;All right reserved &nbsp;Terms of Use</div>

</body>
</html>
```